Brightwell Giving Inc

We need a full re-design of our non-profit organization website (www.brightwellgiving.org). Ideally, we are looking to make it more attractive, user-friendly, and interactive with our business model.

Please make sure to user colors that ago with our logo.

We need a homepage done and we also need a content page done where we will use for the other pages to fill with content.

Target Market(s)

Clothes/textiles donations.

Industry/Entity Type

Charity

Number of Pages Required

2 page

Colors

Designer to choose colors to be used in the design.

Requirements
Must have
• It must match the styling of our logo and same colors as current website. (www.brightwellgiving.org)
Nice to have
• Sleek homepage that is easy to understand and get our main points across.

```html
<!DOCTYPE html>
<html lang="en">
<head>
<meta charset="utf-8">
<title>About Us – Brightwell Giving</title>
<link rel="stylesheet" href="https://fonts.googleapis.com/css2?family=Montserrat:wght@300;400;500;600;700&family=Dancing+Script:wght@600&display=swap">
<style>
:root{
  --yellow:#fdc90c;
  --red:#e0201f;
  --green:#3d6b1f;
  --green-dark:#2f5a17;
  --text:#555;
  --heading:#333;
  --line:#bbb;
  --black:#111;
}
*{box-sizing:border-box;margin:0;padding:0}
html,body{width:796px;height:1200px;overflow:hidden;background:#fff;font-family:'Montserrat',sans-serif;color:var(--text)}
.page{position:relative;width:796px;height:1200px}
.topbar{position:absolute;left:0;top:0;width:796px;height:19px;background:var(--yellow);color:#fff;font-size:8px;text-align:right;padding:5px 58px 0 0}
.topbar span{margin:0 6px}
.nav{position:absolute;top:19px;left:0;width:796px;height:44px;display:flex;align-items:center;justify-content:space-between;padding:0 57px}
.brand{display:flex;align-items:center;gap:6px;font-weight:700;font-size:11px;color:var(--green);letter-spacing:.3px}
.brand i{display:block;width:14px;height:14px;background:var(--yellow);border-radius:50%}
.menu{display:flex;gap:16px;font-size:9px;color:#222}
.menu a{position:relative;color:inherit;text-decoration:none;height:44px;line-height:44px}
.menu a.home{color:var(--red)}
.menu a.active::after{content:"";position:absolute;left:0;right:0;bottom:0;height:3px;background:var(--red)}
.hero{position:absolute;top:63px;left:0;width:796px;height:166px;background:linear-gradient(90deg,#3a3f4a,#5a5f66 45%,#3c4250);display:flex;flex-direction:column;align-items:center;justify-content:center;color:#fff}
.hero h1{font-size:20px;font-weight:700;margin-bottom:3px}
.crumb{font-size:8.5px;display:flex;align-items:center;gap:8px}
.crumb::before,.crumb::after{content:"";width:20px;height:1px;background:#ddd}
.main{position:absolute;left:57px;top:265px;width:440px}
h2{font-size:14px;font-weight:600;color:var(--heading);position:relative;padding-bottom:8px}
h2::after{content:"";position:absolute;left:0;bottom:0;width:22px;height:1px;background:var(--red)}
p{font-size:8.8px;line-height:14.4px;font-weight:300}
.who p{margin-top:8px}
.about{display:flex;gap:16px;margin-top:26px}
.photo{flex:none;background:linear-gradient(135deg,#e6ddd0,#c9b9a3)}
.about .photo{width:148px;height:172px}
.about h2{margin-top:-2px}
.about p{margin-top:9px}
.about p+p{margin-top:14px}
h3{font-size:11px;font-weight:600;color:var(--green);margin-top:18px}
.history p{margin-top:6px}
.history p+p{margin-top:14px}
.side{position:absolute;left:526px;top:270px;width:213px}
.donate{height:155px;background:linear-gradient(135deg,#fcd64a,#f6c21a);text-align:center;padding-top:14px}
.donate .script{font-family:'Dancing Script',cursive;font-size:15px;color:#333}
.donate .big{font-size:23px;font-weight:700;color:var(--red);line-height:28px}
.btn-donate{display:inline-flex;align-items:center;gap:6px;margin-top:14px;background:var(--green-dark);color:#fff;font-size:10px;font-weight:600;border-radius:16px;padding:9px 18px}
.bins{margin-top:25px}
.bins .head{height:32px;background:var(--green);color:#fff;font-size:10.5px;font-weight:600;padding:9px 10px}
.map{height:262px;background:linear-gradient(160deg,#f1ead9,#e8e0c8 60%,#cfdfe8)}
.mission{position:absolute;left:57px;top:757px;width:682px}
.mission .photo{position:absolute;left:0;top:0;width:185px;height:228px;background:linear-gradient(160deg,#a9b7a4,#3f9a3a 55%,#5d6461)}
.mission .copy{position:absolute;left:202px;top:0;width:480px}
.lead{font-size:11px;color:#333;font-weight:500}
.mission h4{font-size:17px;color:var(--green);font-weight:600;position:relative;padding-bottom:8px}
.mission h4::after{content:"";position:absolute;left:0;bottom:0;width:25px;height:1px;background:var(--red)}
.files{display:grid;grid-template-columns:232px 232px;gap:10px 16px;margin-top:17px}
.file{height:50px;border:1px solid var(--line);display:flex;align-items:center;gap:10px;padding-left:16px;font-size:10.5px;color:#333;font-weight:500}
.news{position:absolute;top:1020px;left:0;width:796px;text-align:center}
.news h2{font-size:17px;display:inline-block;padding-bottom:0}
.news h2::after{display:none}
.news .mark{margin-top:8px}
.form{display:flex;justify-content:center;gap:7px;margin-top:14px}
.form .input{width:334px;height:36px;border:1px solid #ccc;border-radius:18px;font-size:8.5px;color:#888;text-align:left;padding:12px 18px}
.form .btn{width:104px;height:35px;border-radius:18px;background:var(--yellow);color:#fff;font-size:11px;font-weight:600;line-height:35px}
.footer{position:absolute;left:0;top:1151px;width:796px;height:49px;background:var(--black);color:#ccc;font-size:8px}
.footer .badge{position:absolute;left:57px;top:3px;width:42px;height:42px;border-radius:50%;background:var(--yellow)}
.footer .copy{position:absolute;right:58px;top:20px}
</style>
</head>
<body>
<div class="page">
  <div class="topbar">Toll Free: (855) 555-0142<span>|</span>New York: 518-555-0190</div>
  <header class="nav">
    <div class="brand"><i></i>BRIGHTWELL GIVING</div>
    <nav class="menu">
      <a class="home">Home</a><a>Missions</a><a>Family</a><a>How it works</a><a class="active">About US</a><a>Sponsors</a><a>News</a><a>Donate</a><a>Wall of needs</a>
    </nav>
  </header>
  <section class="hero" role="img" aria-label="Volunteers sorting donated clothing into boxes">
    <h1>About Us</h1>
    <div class="crumb">Home » About Us</div>
  </section>

  <main class="main">
    <div class="who">
      <h2>Who We Are</h2>
      <p>Sed ut perspiciatis unde omnis iste natus error sit voluptatem accusantium doloremque laudantium, totam rem aperiam, eaque ipsa quae ab illo inventore veritatis et quasi architecto beatae vitae dicta sunt explicabo. Nemo enim ipsam voluptatem quia voluptas sit aspernatur aut odit aut fugit, sed quia consequuntur magni dolores eos qui ratione voluptatem sequi nesciunt. Neque porro quisquam est, qui dolorem ipsum quia dolor sit amet.</p>
    </div>
    <div class="about">
      <div class="photo" role="img" aria-label="Smiling volunteers with a donations box"></div>
      <div>
        <h2>About Brightwell Giving</h2>
        <p>Sed ut perspiciatis unde omnis iste natus error sit voluptatem accusantium doloremque laudantium, totam rem aperiam, eaque ipsa quae ab illo inventore veritatis et quasi architecto beatae vitae dicta sunt explicabo.</p>
        <p>Nemo enim ipsam voluptatem quia voluptas sit aspernatur aut odit aut fugit, sed quia consequuntur magni dolores eos qui ratione voluptatem sequi nesciunt. Neque porro quisquam est, qui dolorem ipsum quia dolor sit amet.</p>
      </div>
    </div>
    <div class="history">
      <h3>History Of Brightwell Giving</h3>
      <p>Sed ut perspiciatis unde omnis iste natus error sit voluptatem accusantium doloremque laudantium, totam rem aperiam, eaque ipsa quae ab illo inventore veritatis et quasi architecto beatae vitae dicta sunt explicabo.</p>
      <p>Nemo enim ipsam voluptatem quia voluptas sit aspernatur aut odit aut fugit, sed quia consequuntur magni dolores eos qui ratione voluptatem sequi nesciunt. Neque porro quisquam est, qui dolorem ipsum quia dolor sit amet.</p>
    </div>
  </main>

  <aside class="side">
    <div class="donate">
      <div class="script">Make a</div>
      <div class="big">Donation</div>
      <div class="script">Thank you!</div>
      <div class="btn-donate">
        <svg width="11" height="10" viewBox="0 0 24 22"><path d="M12 21 2.5 11.5A5.7 5.7 0 0 1 12 3.6a5.7 5.7 0 0 1 9.5 7.9z" fill="#fff"/></svg>
        Donate Now
      </div>
    </div>
    <div class="bins">
      <div class="head">Brightwell Giving Bins</div>
      <div class="map" role="img" aria-label="Map of donation bin locations across the region"></div>
    </div>
  </aside>

  <section class="mission">
    <div class="photo" role="img" aria-label="Green clothing and shoes donation bin"></div>
    <div class="copy">
      <div class="lead">Please take a small step and</div>
      <h4>Help us with our mission</h4>
      <div class="files">
        <div class="file"><svg width="22" height="20" viewBox="0 0 22 20"><path d="M4 1h10l4 4v14H4z" fill="none" stroke="#6a9a3a"/><rect x="1" y="9" width="14" height="7" fill="#fff" stroke="#6a9a3a"/><text x="3" y="15" font-size="5" fill="#6a9a3a" font-family="Montserrat,sans-serif">PDF</text></svg>At vero eos et accusamus et</div>
        <div class="file"><svg width="22" height="20" viewBox="0 0 22 20"><path d="M4 1h10l4 4v14H4z" fill="none" stroke="#6a9a3a"/><rect x="1" y="9" width="14" height="7" fill="#fff" stroke="#6a9a3a"/><text x="3" y="15" font-size="5" fill="#6a9a3a" font-family="Montserrat,sans-serif">PDF</text></svg>At vero eos et accusamus et</div>
        <div class="file"><svg width="22" height="20" viewBox="0 0 22 20"><path d="M4 1h10l4 4v14H4z" fill="none" stroke="#6a9a3a"/><rect x="1" y="9" width="14" height="7" fill="#fff" stroke="#6a9a3a"/><text x="3" y="15" font-size="5" fill="#6a9a3a" font-family="Montserrat,sans-serif">PDF</text></svg>At vero eos et accusamus et</div>
        <div class="file"><svg width="22" height="20" viewBox="0 0 22 20"><path d="M4 1h10l4 4v14H4z" fill="none" stroke="#6a9a3a"/><rect x="1" y="9" width="14" height="7" fill="#fff" stroke="#6a9a3a"/><text x="3" y="15" font-size="5" fill="#6a9a3a" font-family="Montserrat,sans-serif">PDF</text></svg>At vero eos et accusamus et</div>
        <div class="file"><svg width="22" height="20" viewBox="0 0 22 20"><path d="M4 1h10l4 4v14H4z" fill="none" stroke="#6a9a3a"/><rect x="1" y="9" width="14" height="7" fill="#fff" stroke="#6a9a3a"/><text x="3" y="15" font-size="5" fill="#6a9a3a" font-family="Montserrat,sans-serif">PDF</text></svg>At vero eos et accusamus et</div>
        <div class="file"><svg width="22" height="20" viewBox="0 0 22 20"><path d="M4 1h10l4 4v14H4z" fill="none" stroke="#6a9a3a"/><rect x="1" y="9" width="14" height="7" fill="#fff" stroke="#6a9a3a"/><text x="3" y="15" font-size="5" fill="#6a9a3a" font-family="Montserrat,sans-serif">PDF</text></svg>At vero eos et accusamus et</div>
      </div>
    </div>
  </section>

  <section class="news">
    <h2>Subscribe to Our Newsletter!</h2>
    <div class="mark"><svg width="80" height="12" viewBox="0 0 80 12"><line x1="0" y1="6" x2="32" y2="6" stroke="#e0201f"/><line x1="48" y1="6" x2="80" y2="6" stroke="#e0201f"/><path d="M40 11.5 34.5 6A3.2 3.2 0 0 1 40 2a3.2 3.2 0 0 1 5.5 4z" fill="#e0201f"/></svg></div>
    <div class="form">
      <div class="input">Your Email Address</div>
      <div class="btn">Subscribe</div>
    </div>
  </section>

  <footer class="footer">
    <div class="badge"></div>
    <div class="copy">© 2018 Brightwell Giving. All Rights Reserved.</div>
  </footer>
</div>
</body>
</html>
```